QM Fenwold Detailing, Inc.

I'm looking for business card design for an existing company with an existing logo/website. www.qmfenwold-detailing.com. VETERAN OWNED logo must be present.

Target Market(s)

Structural and architectural steel fabricators

Industry/Entity Type

Structural and architectural steel detailing and engineering

Contact Information for Business Card

logo, business name, address, phone, website, email, employee info

Font styles to use
Serif

Colors
00AB8E
00BBA5
67D7C9
C6EFE9
E9F9F6

Requirements
Must have
• company logo, website, VETERAN OWNED LOGO
Should not have
• Don't make it too busy. Less is more

```html
<!DOCTYPE html>
<html lang="en">
<head>
<meta charset="utf-8">
<title>QM Fenwold Detailing — Business Card</title>
<link rel="stylesheet" href="https://fonts.googleapis.com/css2?family=Open+Sans:wght@400;600;700&display=swap">
<style>
  :root {
    --teal-deep: #1f7f85;
    --teal-card: #56c0c0;
    --teal-dark: #2a6f78;
    --ink: #333b40;
    --paper: #f7f8f8;
    --bg-top: #c9ced6;
    --bg-bottom: #e9ecef;
    --badge-red: #d63a3a;
    --badge-blue: #2f4f9a;
  }
  * { box-sizing: border-box; margin: 0; padding: 0; }
  html, body { width: 1200px; height: 675px; overflow: hidden; }
  body {
    background: linear-gradient(160deg, var(--bg-bottom), var(--bg-top));
    font-family: "Open Sans", Arial, sans-serif;
    display: flex; align-items: center; justify-content: center; gap: 48px;
  }
  .card {
    width: 520px; height: 297px; position: relative;
    box-shadow: 0 10px 28px rgba(40, 60, 80, .22);
  }
  .card--front {
    background: var(--teal-card);
    display: flex; align-items: center; justify-content: center;
  }
  .brand-front {
    color: #ffffff; font-weight: 700; font-size: 30px; letter-spacing: 2px;
    text-align: center; line-height: 1.2;
  }
  .card--back { background: var(--paper); }
  .holder { position: absolute; left: 40px; top: 62px; }
  .holder__name {
    color: var(--teal-dark); font-weight: 700; font-size: 21px; letter-spacing: .5px;
  }
  .holder__role {
    color: var(--ink); font-size: 12px; margin-top: 2px; padding-bottom: 4px;
    border-bottom: 2px solid var(--teal-deep); display: inline-block; width: 52px;
  }
  .brand-back {
    position: absolute; right: 34px; top: 34px; width: 170px;
    color: var(--teal-deep); font-weight: 700; font-size: 19px; letter-spacing: 1px;
    line-height: 1.15; text-align: center;
  }
  .veteran-badge { position: absolute; right: 50px; top: 140px; }
  .contact {
    position: absolute; left: 40px; top: 170px; color: var(--ink);
    font-size: 12.5px; line-height: 1.45;
  }
  .contact__address { margin-bottom: 10px; }
  .contact__row { display: flex; align-items: center; gap: 8px; }
  .contact__row svg { width: 12px; height: 12px; flex: none; }
  .contact__phone { letter-spacing: 2px; }
</style>
</head>
<body>
  <section class="card card--front">
    <div class="brand-front">QM FENWOLD<br>DETAILING</div>
  </section>

  <section class="card card--back">
    <div class="holder">
      <div class="holder__name">DORIAN VELASCO</div>
      <div class="holder__role">Founder</div>
    </div>

    <div class="brand-back">QM FENWOLD<br>DETAILING</div>

    <svg class="veteran-badge" width="130" height="100" viewBox="0 0 130 100" role="img" aria-label="Veteran owned business badge">
      <circle cx="65" cy="50" r="46" fill="none" stroke="var(--badge-blue)" stroke-width="4"/>
      <circle cx="65" cy="50" r="36" fill="var(--badge-red)" opacity=".85"/>
    </svg>

    <div class="contact">
      <p class="contact__address">4410 Harbor Crest Ave., ste 310<br>Larkport, FL 33990</p>
      <p class="contact__row contact__phone">
        <svg viewBox="0 0 24 24"><path fill="var(--teal-deep)" d="M6.6 10.8a15 15 0 0 0 6.6 6.6l2.2-2.2a1 1 0 0 1 1-.25 11.4 11.4 0 0 0 3.6.57 1 1 0 0 1 1 1V20a1 1 0 0 1-1 1A17 17 0 0 1 3 4a1 1 0 0 1 1-1h3.5a1 1 0 0 1 1 1c0 1.25.2 2.45.57 3.57a1 1 0 0 1-.25 1z"/></svg>
        555.014.2287
      </p>
      <p class="contact__row">
        <svg viewBox="0 0 24 24"><rect x="2" y="5" width="20" height="14" fill="var(--teal-deep)"/><path d="M2 5l10 8 10-8" fill="none" stroke="#fff" stroke-width="2"/></svg>
        sales@qmfenwold-detailing.com
      </p>
      <p class="contact__row">
        <svg viewBox="0 0 24 24"><circle cx="12" cy="12" r="10" fill="none" stroke="var(--teal-deep)" stroke-width="2"/><path d="M2 12h20M12 2c3 3 3 17 0 20M12 2c-3 3-3 17 0 20" fill="none" stroke="var(--teal-deep)" stroke-width="1.6"/></svg>
        www.qmfenwold-detailing.com
      </p>
    </div>
  </section>
</body>
</html>
```